The Brightway Surgery Stationary (Medical)

Stationery for The Brightway surgery
using existing logos
Please also add a green apple if possible on another corner away from the logo on some of your designs

Please take a look at www.thebrightwaysurgery.com.au so you can get a feel for what The Brightway Surgery offers our clients.

Stationary Required: business cards, letter head, comp slips

I do not require envelopes or invoives.

Target Market(s)

The general popultation needing medical care
Professionals
Mums & Dads
Elderly

Industry/Entity Type

Business

Requirements
Must have
• Company Logo

Address
Email
Website
Phone
Should not have
• Traditional Medical Icons
No Times New Roman

```html
<!DOCTYPE html>
<html lang="en">
<head>
<meta charset="utf-8">
<title>The Brightway Surgery – Business Card</title>
<link href="https://fonts.googleapis.com/css2?family=Quicksand:wght@500;600&display=swap" rel="stylesheet">
<style>
  :root {
    --sky: #00aeef;
    --sky-light: #8fd6f5;
    --leaf: #a6ce39;
    --leaf-light: #d6e59c;
    --ink: #4a4a4a;
    --paper: #ffffff;
    --edge: #9fd9f2;
  }
  * { margin: 0; padding: 0; box-sizing: border-box; }
  html, body { width: 911px; height: 1200px; overflow: hidden; background: var(--paper); }
  body { position: relative; font-family: "Quicksand", sans-serif; color: var(--ink); }

  .card {
    position: absolute; left: 93px; width: 727px; height: 415px;
    background: var(--paper); border: 1px solid var(--edge); overflow: hidden;
  }
  .card--front { top: 93px; }
  .card--back { top: 692px; height: 416px; }
  .card__shapes { position: absolute; inset: 0; width: 100%; height: 100%; }

  .brand {
    position: absolute; display: flex; align-items: center; gap: 12px;
    color: var(--sky); font-weight: 600; line-height: 1.05;
  }
  .brand__dot { width: 30px; height: 30px; border-radius: 50%; background: var(--leaf); flex: none; }
  .brand__name { font-size: 27px; }
  .card--front .brand { left: 40px; top: 158px; }
  .card--back .brand { left: 440px; top: 248px; }
  .card--back .brand__name { font-size: 31px; }

  .divider { position: absolute; left: 300px; top: 125px; width: 4px; height: 172px; background: var(--leaf); }

  .contact { position: absolute; left: 330px; top: 134px; font-size: 19.5px; font-weight: 500; line-height: 27px; }
  .contact__line { display: flex; align-items: center; gap: 8px; }
  .contact__line svg { flex: none; }
  .contact__address { margin-bottom: 6px; }
  .contact__phone { margin-bottom: 4px; }

  .apple { position: absolute; left: 647px; top: 300px; width: 32px; height: 36px; border-radius: 50% 50% 45% 45%; background: var(--leaf); }

  .website { position: absolute; right: 38px; top: 367px; font-size: 21px; font-weight: 500; color: var(--paper); }
</style>
</head>
<body>

<section class="card card--front">
  <svg class="card__shapes" viewBox="0 0 526 300" preserveAspectRatio="none" aria-hidden="true">
    <path d="M0,0 H526 V52 C400,85 300,20 150,20 C80,20 30,35 0,45 Z" fill="var(--sky)"/>
    <path d="M0,45 C30,35 80,20 150,20 C300,20 400,85 526,52 V58 C380,100 230,45 120,62 C60,72 20,90 0,100 Z" fill="var(--sky-light)"/>
    <path d="M0,258 C70,232 170,235 250,258 L250,300 L0,300 Z" fill="var(--leaf-light)"/>
    <path d="M0,300 C110,262 300,240 526,266 V300 Z" fill="var(--leaf)"/>
  </svg>

  <div class="brand">
    <span class="brand__dot"></span>
    <span class="brand__name">The Brightway<br>Surgery</span>
  </div>

  <div class="divider"></div>

  <div class="contact">
    <p class="contact__address">Shop 4, Brightway Village Centre<br>18 - 24 Maple Grove Road<br>Brightway 2199</p>
    <p class="contact__line contact__phone">
      <svg width="22" height="20" viewBox="0 0 22 20" aria-hidden="true"><path d="M6,3 C3,6 4,12 9,16 L11,14 L8,11 L9,9 L7,5 Z" fill="var(--sky)"/></svg>
      02 5550 1842
    </p>
    <p class="contact__line">
      <svg width="26" height="20" viewBox="0 0 26 20" aria-hidden="true"><rect x="1" y="2" width="24" height="16" fill="none" stroke="var(--sky)" stroke-width="1.5"/><path d="M1,2 L13,12 L25,2" fill="none" stroke="var(--sky)" stroke-width="1.5"/></svg>
      hello@thebrightwaysurgery.com.au
    </p>
  </div>

  <div class="apple" role="img" aria-label="Small green apple"></div>

  <p class="website">www.thebrightwaysurgery.com.au</p>
</section>

<section class="card card--back">
  <svg class="card__shapes" viewBox="0 0 526 301" preserveAspectRatio="none" aria-hidden="true">
    <path d="M0,0 H40 C50,170 250,282 526,276 V301 H0 Z" fill="var(--sky-light)"/>
    <path d="M0,65 C40,210 230,290 420,291 C470,291 500,290 526,289 V301 H0 Z" fill="var(--sky)"/>
  </svg>

  <div class="brand">
    <span class="brand__dot"></span>
    <span class="brand__name">The Brightway<br>Surgery</span>
  </div>
</section>

</body>
</html>
```